IT company website design

Require a home page and an inner page designed for a company located in Ohio. The company deals with a wide range of IT services like Software development, IT based education services such as digital textbooks and BPO

Would like to get a Home page for the website and an inner page to be designed.

Design must be modern, clean and very professional. The home page should have a carousel of our services for which content will be provided.

It should give a feel that we are a large company to our prospective customers.
Updates

Hi,
In the few designs I have got for the home page, there are mockups with unwanted content/blocks like ex. latest blog posts or similar blocks. Kindly note that, we don't want this. Please follow the information about content on the home page as mentioned in the project brief. Designers, who have already submitted designs, if you can remove the unwanted blocks, it will be really appreciated.

Thanks.

I have received over 9 designs for this project, but none of them seem to be custom designed for my needs. They are just re-use of previous designs and look very out dated. Looking for fresh, clean designs following latest design trends like the ones you see in gridmarket etc.

If you can provide me a design that meets my expectations, I can definitely UP my budget for you .

Industry/Entity Type

Education

Requirements
Must have
• > > Home page > >
Home page will have

* Top Menu: Home, About Us, Solutions, Services, Contact us (should have space to accommodate for more)

* Should have a flash carousel/slide show. Each slide should be about a service we provide. Ex. a slide for bpo will have the content "Bridging the quality and cost divide in outsourcing" It should be depicted by an illustration or photograph. If you are going to use photograph, please use ones for pixvaultimages.com

* Textual content of about 200 words which we will provide

* Links in the footer along with a copyright, legal notice etc.

* Importantly, the home page should have 2 fancy buttons for "Member Login" and "Online Tutoring"

> > Inner pages > >
Will be mainly textual content explaining each of the service so, should have space for lots of textual content, with a fancy, page title (usually the service name). All inner pages should also have a side menu or something like that from where users can have a one click access to all our services.

Our logo is blue in color. with color code "0080FB". It just a stylized D with rest of the text i.e Varnex Tek Inc. our logo is of the proportion. 1:5 i.e 60px height, 300px wide. We can proportionately increase or decrease the dimensions as necessary. Color combination of the sight should be something that will go with this.

```html
<!DOCTYPE html>
<html lang="en">
<head>
<meta charset="utf-8">
<title>Varnex Tek Inc – Home</title>
<link href="https://fonts.googleapis.com/css2?family=Arimo:wght@400;700&display=swap" rel="stylesheet">
<style>
  :root {
    --brand-blue: #0080fb;
    --nav-text: #222222;
    --heading-grey: #444444;
    --body-grey: #3c3c3c;
    --footer-grey: #7a7a7a;
    --frame-grey: #e2e2e2;
    --band-light: #f7f7f7;
    --band-mid: #ececec;
    --hatch-a: #d4d4d4;
    --hatch-b: #f2f2f2;
    --slide-dark: #2a2a2a;
    --slide-mid: #6a6a6a;
    --visual-top: #3a4654;
    --visual-bottom: #26323f;
    --button-top: #3aa2ff;
    --button-bottom: #0062d6;
    --white: #ffffff;
  }
  html, body {
    margin: 0;
    padding: 0;
    overflow: hidden;
    background: var(--white);
  }
  .page {
    position: relative;
    width: 1200px;
    height: 883px;
    overflow: hidden;
    font-family: "Arimo", Arial, sans-serif;
    background: var(--white);
  }

  /* Header */
  .site-header {
    position: absolute;
    left: 0; top: 0;
    width: 1200px; height: 82px;
    background: linear-gradient(to bottom, var(--white), var(--band-mid));
  }
  .hatch-band {
    position: absolute;
    left: 0;
    width: 1200px;
    background: repeating-linear-gradient(45deg, var(--hatch-a) 0 1px, var(--hatch-b) 1px 3px);
  }
  .hatch-band.header-rule { top: 82px; height: 8px; }
  .brand {
    position: absolute;
    left: 176px; top: 18px;
    display: flex;
    align-items: center;
    gap: 14px;
  }
  .brand-mark {
    width: 44px; height: 44px;
    background: var(--brand-blue);
  }
  .brand-name {
    font-size: 30px;
    font-weight: 700;
    color: var(--brand-blue);
    letter-spacing: -1px;
  }
  .main-nav {
    position: absolute;
    left: 525px; top: 43px;
    display: flex;
    align-items: center;
    font-size: 18px;
    color: var(--nav-text);
  }
  .main-nav a {
    color: inherit;
    text-decoration: none;
    padding: 0 6px;
  }
  .main-nav a.is-current { color: var(--brand-blue); }
  .nav-divider { width: 10px; height: 28px; margin: 0 9px; }

  /* Slider */
  .slider-frame {
    position: absolute;
    left: 162px; top: 88px;
    width: 876px; height: 322px;
    background: var(--frame-grey);
  }
  .slider-base {
    position: absolute;
    left: 150px; top: 410px;
    width: 900px; height: 7px;
    background: var(--frame-grey);
  }
  .slider-post {
    position: absolute;
    top: 417px;
    width: 6px; height: 26px;
    background: var(--frame-grey);
  }
  .slider-post.left { left: 162px; }
  .slider-post.right { left: 1032px; }
  .slide {
    position: absolute;
    left: 172px; top: 94px;
    width: 857px; height: 313px;
    background: radial-gradient(ellipse at 60% 40%, var(--slide-mid), var(--slide-dark) 75%);
    color: var(--white);
    overflow: hidden;
  }
  .slide-kicker {
    position: absolute;
    left: 27px; top: 24px;
    margin: 0;
    font-size: 28px;
    font-weight: 700;
    letter-spacing: -0.8px;
  }
  .slide-title {
    position: absolute;
    left: 26px; top: 57px;
    margin: 0;
    font-size: 43px;
    font-weight: 700;
    letter-spacing: -1.6px;
    color: #e6e6e6;
  }
  .slide-text {
    position: absolute;
    left: 28px; top: 113px;
    width: 500px;
    margin: 0;
    font-size: 13px;
    line-height: 20px;
  }
  .slide-visual {
    position: absolute;
    left: 560px; top: 22px;
    width: 266px; height: 262px;
    background: linear-gradient(to bottom, var(--visual-top), var(--visual-bottom));
  }
  .cta {
    position: absolute;
    top: 229px;
    height: 47px;
    border-radius: 24px;
    background: linear-gradient(to bottom, var(--button-top), var(--button-bottom));
    display: flex;
    align-items: center;
    gap: 8px;
    padding-left: 9px;
    box-sizing: border-box;
    font-size: 17px;
    font-weight: 700;
    letter-spacing: -0.8px;
    color: var(--white);
    text-decoration: none;
    white-space: nowrap;
  }
  .cta.member-login { left: 29px; width: 199px; }
  .cta.online-tutoring { left: 260px; width: 208px; }
  .cta-icon { width: 22px; height: 22px; flex: none; }
  .slider-dots {
    position: absolute;
    left: 565px; top: 427px;
    display: flex;
    gap: 10px;
  }
  .slider-dots span {
    width: 12px; height: 12px;
    border-radius: 50%;
    background: radial-gradient(circle at 40% 35%, #dfe5e5, #96a3a3);
  }
  .slider-dots span.is-active { background: radial-gradient(circle at 40% 35%, #f2f2f2, #c2c8c8); }

  /* Welcome content */
  .welcome-title {
    position: absolute;
    left: 171px; top: 481px;
    margin: 0;
    font-size: 24px;
    font-weight: 700;
    letter-spacing: -0.8px;
    color: var(--heading-grey);
  }
  .hatch-band.content-rule { left: 161px; top: 522px; width: 879px; height: 7px; }
  .welcome-copy {
    position: absolute;
    left: 171px; top: 543px;
    width: 858px;
    font-size: 12px;
    line-height: 20px;
    letter-spacing: 0.15px;
    color: var(--body-grey);
    text-align: justify;
  }
  .welcome-copy p { margin: 0 0 20px; }

  /* Footer */
  .hatch-band.footer-rule { top: 776px; height: 10px; }
  .site-footer {
    position: absolute;
    left: 0; top: 786px;
    width: 1200px; height: 97px;
    background: linear-gradient(to bottom, var(--band-mid), var(--white));
  }
  .footer-brand {
    position: absolute;
    left: 176px; top: 20px;
    display: flex;
    align-items: center;
    gap: 9px;
    font-size: 19px;
    font-weight: 700;
    letter-spacing: -0.5px;
    color: var(--footer-grey);
  }
  .footer-brand .brand-mark {
    width: 28px; height: 28px;
    background: var(--footer-grey);
  }
  .footer-links {
    position: absolute;
    right: 161px; top: 26px;
    font-size: 12px;
    color: var(--footer-grey);
  }
  .footer-links a { color: inherit; text-decoration: none; }
  .footer-links .sep { margin: 0 14px; }
</style>
</head>
<body>
<div class="page">

  <header class="site-header">
    <div class="brand">
      <span class="brand-mark"></span>
      <span class="brand-name">Varnex Tek Inc</span>
    </div>
    <nav class="main-nav">
      <a class="is-current" href="#">home</a>
      <svg class="nav-divider" viewBox="0 0 10 28"><line x1="9" y1="1" x2="1" y2="27" stroke="#c8c8c8" stroke-width="1.5"/></svg>
      <a href="#">about us</a>
      <svg class="nav-divider" viewBox="0 0 10 28"><line x1="9" y1="1" x2="1" y2="27" stroke="#c8c8c8" stroke-width="1.5"/></svg>
      <a href="#">solutions</a>
      <svg class="nav-divider" viewBox="0 0 10 28"><line x1="9" y1="1" x2="1" y2="27" stroke="#c8c8c8" stroke-width="1.5"/></svg>
      <a href="#">services</a>
      <svg class="nav-divider" viewBox="0 0 10 28"><line x1="9" y1="1" x2="1" y2="27" stroke="#c8c8c8" stroke-width="1.5"/></svg>
      <a href="#">contact us</a>
    </nav>
  </header>
  <div class="hatch-band header-rule"></div>

  <section class="services-slider">
    <div class="slider-frame"></div>
    <div class="slider-base"></div>
    <div class="slider-post left"></div>
    <div class="slider-post right"></div>
    <div class="slide">
      <h2 class="slide-kicker">Bridging the quality and</h2>
      <h1 class="slide-title">cost divide in outsourcing</h1>
      <p class="slide-text">Lorem ipsum dolor sit amet, consectetur adipiscing elit. Duis facilisis scelerisque imperdiet. Donec sem turpis, euismod bibendum tempus id, dignissim quis justo. In hac habitasse platea dictumstMaecenas ut nibh odio, eu lacinia felis.</p>
      <a class="cta member-login" href="#">
        <svg class="cta-icon" viewBox="0 0 22 22"><circle cx="11" cy="11" r="10" fill="#8cc8ff"/><path d="M6 9h6V5.5l5 5.5-5 5.5V13H6z" fill="#ffffff"/></svg>
        MEMBER LOGIN
      </a>
      <a class="cta online-tutoring" href="#">
        <svg class="cta-icon" viewBox="0 0 22 22"><circle cx="11" cy="11" r="10" fill="#8cc8ff"/><path d="M6 9h6V5.5l5 5.5-5 5.5V13H6z" fill="#ffffff"/></svg>
        ONLINE TUTORING
      </a>
      <div class="slide-visual" role="img" aria-label="Illustration of a glowing blue glass globe with a dotted world map"></div>
    </div>
    <div class="slider-dots">
      <span class="is-active"></span><span></span><span></span><span></span>
    </div>
  </section>

  <main>
    <h2 class="welcome-title">Welcome to varnex tek inc</h2>
    <div class="hatch-band content-rule"></div>
    <div class="welcome-copy">
      <p>Lorem ipsum dolor sit amet, consectetur adipiscing elit. Duis facilisis scelerisque imperdiet. Donec sem turpis, euismod bibendum tempus id, quis justo. In hac habitasse platea dictumst. Maecenas ut nibh odio, eu lacinia felis. Curabitur lorem odio, dictum sed pellentesque in, tincidunt quis turpis. Donec cursus consectetur feugiat. Morbi cursus quam eget sapien porttitor elementum. Curabitur ut ligula magna, vitae auctor velit. Nullam hendrerit mattis purus, vitae pulvinar justo tempor at. Curabitur accumsan magna vitae nisl venenatis consectetur.</p>
      <p>Morbi sagittis varius orci at porttitor. Cras sed urna sapien. Praesent magna ante, pretium non tincidunt in, fermentum et purus. Morbi vestibulum nunc in ipsum suscipit volutpat. Sed ac ipsum nibh. Pellentesque odio lorem, ullamcorper eget hendrerit sollicitudin, dictum eu neque. Curabitur blandit elementum orci sed viverra. Vestibulum auctor ullamcorper ipsum, in egestas augue rhoncus non. Vestibulum eu erat nec leo porttitor aliquam. Etiam eget mi tellus, sed suscipit mi. Suspendisse semper faucibus felis vitae mattis. Sed tempor scelerisque dolor, in iaculis tellus auctor nec. Vestibulum lectus dui, ullamcorper sed fringilla et, blandit vel metus.</p>
    </div>
  </main>

  <div class="hatch-band footer-rule"></div>
  <footer class="site-footer">
    <div class="footer-brand">
      <span class="brand-mark"></span>
      <span>Varnex Tek Inc</span>
    </div>
    <div class="footer-links">
      <span>© 2011 varnex tek inc. all rights reserved.</span>
      <span class="sep">|</span>
      <a href="#">terms of service</a>
      <span class="sep">|</span>
      <a href="#">privacy policy</a>
    </div>
  </footer>

</div>
</body>
</html>
```